Modern Academic Informational Postcard and Graphic

I am looking for a postcard design, with a fast turnaround time (24-hours). These postcards will be handed out at a presentation that is being given as part of an interview process. I would like to print two information cards per 8.5/11 piece of paper. These cards will be double sided. The front side is a visual graphic representing the 4 elements of the vision this interview candidate plans to bring to the position. The backside includes a snapshot of this candidate’s academic and administrative background. I have attached a sketch of the front and back sides. There should also be a simple visual on the backside denoting a spot reserved for Marlowe College (MC) on this career continuum (on the sketch this is represented by a star with MC in the middle).

I would like the crimson palatte to be used (https://www.marlowecollege-example.org/brand/design/color.html) and, if possible Benton Sans font. And the overall aesthetic should be modern and minimalistic, and convey professionalism. The information does not have to be presented in the way that it is in the attached documents (this was just a rough sketch/idea).

```html
<!DOCTYPE html>
<html lang="en">
<head>
<meta charset="utf-8">
<title>Dana R. Whitfield — Vision and Background Cards</title>
<link rel="stylesheet" href="https://fonts.googleapis.com/css2?family=Oswald:wght@400;500;600&family=Montserrat:wght@600;700&family=Roboto+Condensed:wght@300;400&display=swap">
<style>
  :root{
    --backdrop:#0b1b27;
    --card:#f1f1f3;
    --card-edge:#dcdcdf;
    --navy:#1c4677;
    --navy-deep:#132c4a;
    --indigo:#2b3590;
    --magenta:#d81b72;
    --crimson:#990000;
    --crimson-dark:#5e0a0a;
    --orange:#f28a1b;
    --teal:#1fb0c6;
    --ink:#4a4a4f;
    --ink-soft:#6b6b70;
    --row-a:#d5d5d8;
    --row-b:#e3e3e6;
    --rule:#bdbdc2;
  }
  *{box-sizing:border-box;margin:0;padding:0}
  html,body{width:960px;height:1200px;overflow:hidden}
  body{background:var(--backdrop);position:relative;font-family:"Roboto Condensed",sans-serif}

  .card{position:absolute;left:130px;width:700px;height:542px;
    background:linear-gradient(110deg,#ffffff 0%,var(--card) 55%,var(--card-edge) 100%);
    box-shadow:0 6px 18px rgba(0,0,0,.35)}
  .card--front{top:36px}
  .card--back{top:620px}

  .card__frame{position:absolute;inset:20px;border:1.5px solid var(--navy-deep)}

  /* vision diagram */
  .vision{position:absolute;left:0;top:0;width:700px;height:542px}
  .node-label{position:absolute;width:120px;text-align:center;font-family:"Oswald",sans-serif;
    font-weight:600;font-size:13.5px;line-height:1.2;color:var(--ink);text-transform:uppercase}
  .node-label--org{left:297px;top:108px}
  .node-label--outreach{left:458px;top:275px}
  .node-label--assess{left:297px;top:430px}
  .node-label--student{left:136px;top:275px}
  .core-label{position:absolute;left:297px;top:278px;width:120px;text-align:center;
    font-family:"Oswald",sans-serif;font-weight:600;font-size:22px;line-height:1.1;color:var(--ink)}

  .brand-mark{position:absolute;display:flex;align-items:center;gap:6px;
    font-family:"Oswald",sans-serif;font-weight:600;font-size:22px;color:var(--crimson)}
  .brand-mark__dot{width:14px;height:14px;border-radius:50%;background:var(--crimson)}
  .card--front .brand-mark{left:588px;top:418px}
  .contact{position:absolute;font-family:"Roboto Condensed",sans-serif;font-weight:300;font-size:10.5px;color:var(--ink-soft);letter-spacing:.2px}
  .card--front .contact{right:44px;top:460px}

  /* background card */
  .bio{position:absolute;left:0;right:0;top:52px;text-align:center;font-family:"Oswald",sans-serif}
  .bio__name{font-weight:500;font-size:26px;color:var(--indigo);letter-spacing:.2px}
  .bio__title{font-weight:500;font-size:22px;color:var(--ink);margin-top:2px}
  .bio__title small{font-size:15px}

  .timeline{position:absolute;left:40px;top:146px;width:630px;
    display:grid;grid-template-columns:repeat(5,1fr);
    grid-template-rows:62px 62px 86px 38px 56px 30px;
    border:1px solid var(--rule);box-shadow:0 3px 8px rgba(0,0,0,.12)}
  .role{display:flex;align-items:center;justify-content:center;text-align:center;
    font-family:"Montserrat",sans-serif;font-weight:700;font-size:11.5px;line-height:1.2;color:#fff;padding:0 8px}
  .role--teacher{background:linear-gradient(90deg,#0f2640,#1d3f66)}
  .role--professor{background:linear-gradient(90deg,#c4126a,#e63b86)}
  .role--director{background:linear-gradient(90deg,var(--crimson-dark),#b3141a)}
  .role--interim{background:linear-gradient(90deg,#f07b14,#f4a22c)}
  .role--associate{background:linear-gradient(90deg,#2bbcc6,#1a7fb6)}

  .cell{display:flex;align-items:center;justify-content:center;text-align:center;
    font-weight:300;font-size:11px;line-height:1.3;color:var(--ink);text-transform:uppercase;
    padding:0 8px;border-right:1px solid var(--rule)}
  .cell:nth-child(5n){border-right:none}
  .cell--unit{background:var(--row-a)}
  .cell--place{background:var(--row-b)}
  .cell--band{background:var(--row-a)}
  .sector{display:flex;align-items:center;justify-content:center;background:#f3f3f5;
    font-family:"Oswald",sans-serif;font-weight:600;font-size:15px;color:var(--ink-soft)}
  .sector--education{grid-column:1 / span 2;border-right:1px solid var(--rule)}
  .sector--university{grid-column:3 / span 3}
  .timeline__footer{grid-column:1 / -1;background:linear-gradient(90deg,var(--navy-deep),var(--navy));
    display:flex;align-items:center;justify-content:flex-end;padding-right:36px;
    font-family:"Montserrat",sans-serif;font-weight:700;font-size:11px;color:#fff;letter-spacing:.3px}

  .timeline__spot{position:absolute;left:226px;top:338px;width:50px;height:50px;border-radius:50%;
    background:var(--crimson);display:flex;align-items:center;justify-content:center;
    font-family:"Oswald",sans-serif;font-weight:600;font-size:18px;color:#fff;
    box-shadow:0 2px 5px rgba(0,0,0,.25)}
</style>
</head>
<body>

<section class="card card--front" aria-label="Vision card: Inspire Impact">
  <div class="card__frame"></div>
  <svg class="vision" viewBox="0 0 700 542" aria-hidden="true">
    <g transform="translate(357 272)">
      <!-- outer ring arcs -->
      <g fill="none" stroke-width="9" stroke-linecap="butt">
        <path d="M -183 0 A 183 183 0 0 1 0 -183" stroke="var(--orange)"/>
        <path d="M 0 -183 A 183 183 0 0 1 183 0" stroke="var(--navy)"/>
        <path d="M 183 0 A 183 183 0 0 1 0 183" stroke="var(--magenta)"/>
        <path d="M 0 183 A 183 183 0 0 1 -183 0" stroke="var(--teal)"/>
      </g>
      <!-- spokes -->
      <g stroke-width="1" opacity=".55">
        <line x1="-74" y1="-74" x2="-125" y2="-125" stroke="var(--orange)"/>
        <line x1="74" y1="-74" x2="125" y2="-125" stroke="var(--navy)"/>
        <line x1="74" y1="74" x2="125" y2="125" stroke="var(--magenta)"/>
        <line x1="-74" y1="74" x2="-125" y2="125" stroke="var(--teal)"/>
      </g>
      <!-- core halo -->
      <circle r="92" fill="#d9dadf"/>
      <!-- pods -->
      <g>
        <path transform="rotate(0)" fill="var(--navy)" d="M -72 -165 A 72 72 0 0 1 72 -165 C 72 -122 42 -98 32 -70 L -32 -70 C -42 -98 -72 -122 -72 -165 Z"/>
        <path transform="rotate(90)" fill="var(--magenta)" d="M -72 -165 A 72 72 0 0 1 72 -165 C 72 -122 42 -98 32 -70 L -32 -70 C -42 -98 -72 -122 -72 -165 Z"/>
        <path transform="rotate(180)" fill="var(--teal)" d="M -72 -165 A 72 72 0 0 1 72 -165 C 72 -122 42 -98 32 -70 L -32 -70 C -42 -98 -72 -122 -72 -165 Z"/>
        <path transform="rotate(270)" fill="var(--orange)" d="M -72 -165 A 72 72 0 0 1 72 -165 C 72 -122 42 -98 32 -70 L -32 -70 C -42 -98 -72 -122 -72 -165 Z"/>
      </g>
      <g fill="#f6f6f8">
        <circle cx="0" cy="-165" r="60"/>
        <circle cx="165" cy="0" r="60"/>
        <circle cx="0" cy="165" r="60"/>
        <circle cx="-165" cy="0" r="60"/>
        <circle r="70"/>
      </g>
      <!-- people icon -->
      <g transform="translate(0 -196)" fill="none" stroke="var(--navy)" stroke-width="2.4">
        <circle cx="-16" cy="-6" r="6"/><circle cx="16" cy="-6" r="6"/><circle cx="0" cy="-8" r="7"/>
        <path d="M -30 14 C -30 2 -22 2 -16 2 C -10 2 -4 4 -4 8"/>
        <path d="M 30 14 C 30 2 22 2 16 2 C 10 2 4 4 4 8"/>
        <path d="M -14 18 C -14 4 -6 2 0 2 C 6 2 14 4 14 18 Z"/>
      </g>
      <!-- group icon -->
      <g transform="translate(165 -30)" fill="var(--magenta)">
        <circle cx="-12" cy="-10" r="6"/><circle cx="12" cy="-10" r="6"/><circle cx="0" cy="-6" r="7"/>
        <path d="M -22 14 C -22 -2 -14 -2 -12 -2 L -8 -2 L -8 14 Z"/>
        <path d="M 22 14 C 22 -2 14 -2 12 -2 L 8 -2 L 8 14 Z"/>
        <path d="M -10 16 C -10 4 -4 2 0 2 C 4 2 10 4 10 16 Z"/>
      </g>
      <!-- clipboard icon -->
      <g transform="translate(0 132)" fill="none" stroke="var(--teal)" stroke-width="2.2">
        <rect x="-14" y="-18" width="28" height="38" rx="2"/>
        <rect x="-6" y="-22" width="12" height="7" fill="var(--teal)"/>
        <line x1="-4" y1="-8" x2="9" y2="-8"/><line x1="-4" y1="0" x2="9" y2="0"/><line x1="-4" y1="8" x2="9" y2="8"/>
        <rect x="-10" y="-11" width="4" height="4"/><rect x="-10" y="-3" width="4" height="4"/><rect x="-10" y="5" width="4" height="4"/>
      </g>
      <!-- cap icon -->
      <g transform="translate(-165 -30)" fill="var(--orange)">
        <path d="M -26 -6 L 0 -18 L 26 -6 L 0 6 Z"/>
        <path d="M -14 0 L -14 12 C -8 18 8 18 14 12 L 14 0 L 0 7 Z"/>
        <line x1="20" y1="-4" x2="20" y2="12" stroke="var(--orange)" stroke-width="2"/>
        <circle cx="20" cy="14" r="2.5"/>
      </g>
      <!-- bulb icon -->
      <g transform="translate(0 -32)">
        <g stroke="var(--crimson)" stroke-width="2" stroke-linecap="round">
          <line x1="0" y1="-30" x2="0" y2="-24"/><line x1="-20" y1="-20" x2="-15" y2="-15"/><line x1="20" y1="-20" x2="15" y2="-15"/>
          <line x1="-27" y1="0" x2="-21" y2="0"/><line x1="27" y1="0" x2="21" y2="0"/>
          <line x1="-20" y1="20" x2="-15" y2="15"/><line x1="20" y1="20" x2="15" y2="15"/>
        </g>
        <path d="M -11 4 C -17 -4 -13 -17 0 -17 C 13 -17 17 -4 11 4 C 8 8 7 11 7 14 L -7 14 C -7 11 -8 8 -11 4 Z" fill="var(--crimson)"/>
        <rect x="-6" y="16" width="12" height="3" fill="var(--ink)"/>
        <rect x="-5" y="21" width="10" height="3" fill="var(--ink)"/>
      </g>
    </g>
  </svg>
  <p class="node-label node-label--org">Organizational<br>Capacity</p>
  <p class="node-label node-label--outreach">Outreach &amp;<br>Leadership</p>
  <p class="node-label node-label--assess">Assessment &amp;<br>Communication</p>
  <p class="node-label node-label--student">Student<br>Experience</p>
  <p class="core-label">INSPIRE<br>IMPACT</p>
  <div class="brand-mark"><span class="brand-mark__dot"></span>MC</div>
  <p class="contact">DRWHITFIELD@HARLAN.EDU</p>
</section>

<section class="card card--back" aria-label="Academic and administrative background card">
  <header class="bio">
    <h1 class="bio__name">DANA R. WHITFIELD (SHE/HER)</h1>
    <h2 class="bio__title">ACADEMIC <small>AND</small> ADMINISTRATIVE BACKGROUND</h2>
  </header>
  <div class="timeline">
    <div class="role role--teacher">TEACHER</div>
    <div class="role role--professor">PROFESSOR</div>
    <div class="role role--director">DIRECTOR OF ACADEMIC INCLUSION</div>
    <div class="role role--interim">INTERIM VICE PROVOST</div>
    <div class="role role--associate">ASSOCIATE VICE PROVOST</div>

    <div class="cell cell--unit">Brookfield Middle<br>School</div>
    <div class="cell cell--unit">Educational<br>Leadership &amp; Policy<br>Studies</div>
    <div class="cell cell--unit">Office of<br>Diversity &amp; Equity</div>
    <div class="cell cell--unit">Office of<br>Diversity &amp; Equity</div>
    <div class="cell cell--unit">Office of<br>Faculty Affairs</div>

    <div class="cell cell--place">Cedar Valley ISD<br>Fairview, Texas<br>1998-2000</div>
    <div class="cell cell--place">Harlan State Univ.<br>2004 - Present</div>
    <div class="cell cell--place">Harlan State Univ.<br>2018-2019</div>
    <div class="cell cell--place">Harlan State Univ.<br>2019-2021</div>
    <div class="cell cell--place">Harlan State Univ.<br>2021-2023</div>

    <div class="cell cell--band"></div>
    <div class="cell cell--band"></div>
    <div class="cell cell--band"></div>
    <div class="cell cell--band"></div>
    <div class="cell cell--band"></div>

    <div class="sector sector--education">EDUCATION</div>
    <div class="sector sector--university">UNIVERSITY</div>

    <div class="timeline__footer">DRWHITFIELD@HARLAN.EDU</div>
  </div>
  <div class="timeline__spot" aria-label="Marlowe College">MC</div>
</section>

</body>
</html>
```